An eCommerce Business Needs a Wordpress Web Design and Development

We need a website design and development for a new eCommerce business based in New York called "Velvet Ondra". We sell items that are based on satisfying multi-sensory pathways of the person, as we believe that all is interconnected forming the Universal Language. All our products are made of raw natural elements from earth or the cosmos. The final design should communicate visual-perceptive pathways that produce harmonious effects and creativity.
Updates

Dear Designers, Please accept my sincere apology for my delayed response. I am currently in the midst of extensive business travelling while at the same time gathering feedback from online polling with friends as the website potential end-users. I shall get back to you by May 12 or sooner. Thank you for your understanding.

Target Market(s)

Art, fossils, minerals and numismatic collectors.

Industry/Entity Type

Online Shopping

Coding

Coded - Design and coding required

Number of Pages Required

5+ page

Font styles to use
Sans Serif
Script

Colors

Designer to choose colors to be used in the design.

Requirements
Must have
• - Simple and clean design.
• - Desktop and mobile device friendly.
• - Photos and images of string musical instruments, crystals, numismatics and cultural artefacts.
• - A blog page.
• - A check-out cart for online shopping and payment. Example: https://shop.pelmora-example.com
• - Standard links to social media.

```html
<!DOCTYPE html>
<html lang="en">
<head>
<meta charset="utf-8">
<title>Velvet Ondra — Store</title>
<link rel="stylesheet" href="https://fonts.googleapis.com/css2?family=Lato:wght@400;700;900&family=Montserrat:wght@400;500&family=Satisfy&family=Playfair+Display:wght@400&display=swap">
<style>
:root{
  --blue:#0d4d8c;
  --blue-dark:#0a3f73;
  --gold:#a89232;
  --gold-soft:#c9b45a;
  --rust:#b0502d;
  --ink:#2b2b2b;
  --grey:#6b6b6b;
  --teal-1:#2f8f78;
  --teal-2:#5cae98;
  --lav-1:#e6dcea;
  --lav-2:#cdbad8;
  --footer:#1b2422;
  --white:#ffffff;
}
*{box-sizing:border-box;margin:0;padding:0}
html,body{width:1200px;height:2778px;overflow:hidden;background:var(--white)}
body{position:relative;font-family:"Lato",sans-serif;color:var(--ink)}
.abs{position:absolute}
a{color:inherit;text-decoration:none}

/* header */
.site-header{left:0;top:0;width:1200px;height:130px;background:linear-gradient(90deg,#efeee6,#e4e2d6 50%,#ecebe3)}
.brand{left:163px;top:26px;display:flex;align-items:center;gap:10px}
.brand-dot{width:18px;height:18px;border-radius:50%;background:var(--blue)}
.brand-name{font-family:"Lato",sans-serif;font-weight:700;font-size:24px;color:var(--blue);letter-spacing:1px;line-height:28px;width:90px}
.search{left:411px;top:48px;width:215px;height:26px;border:2px solid var(--blue);border-radius:4px;background:#fff;font-family:"Montserrat",sans-serif;font-size:11px;color:#9aa;padding:5px 8px}
.search-btn{left:602px;top:48px;width:26px;height:26px;background:var(--blue);border-radius:0 4px 4px 0}
.top-links{left:709px;top:30px;display:flex;gap:18px;font-size:11px;color:var(--blue);font-family:"Lato",sans-serif}
.top-links .active{color:var(--gold)}
.social{display:flex;gap:12px}
.social span{width:24px;height:24px;border-radius:50%;background:var(--gold)}
.header-social{left:831px;top:85px}
.cart{left:972px;top:84px;width:30px;height:26px}
.cart-info{left:1010px;top:84px;font-size:11px;color:var(--rust);line-height:15px;text-align:center}
.cart-info b{display:block;color:var(--blue);font-weight:400}

/* nav */
.main-nav{left:0;top:130px;width:1200px;height:46px;background:var(--blue)}
.main-nav a{position:absolute;top:16px;font-size:11.5px;font-weight:900;color:#fff;letter-spacing:.3px}
.main-nav a.current{color:var(--gold-soft)}
.dropdown{left:283px;top:180px;width:134px;height:74px;background:#fff;box-shadow:0 2px 6px rgba(0,0,0,.2);padding:8px 22px;font-size:10px;color:var(--gold);line-height:18px}

/* hero */
.hero{left:0;top:176px;width:1200px;height:460px}
.hero-bg{left:0;top:0;width:1200px;height:460px}
.promo{border:2px solid var(--gold-soft);background:rgba(255,255,255,.35)}
.promo-img{position:absolute}
.promo-title{position:absolute;font-family:"Lato",sans-serif;font-weight:700;color:var(--ink)}
.promo-title em{font-style:normal;color:var(--blue)}
.promo-sub{position:absolute;font-family:"Satisfy",cursive;color:var(--ink)}
.promo-sub em{font-style:normal;color:var(--gold)}
.shop-btn{position:absolute;background:#fff;border:2px solid var(--gold-soft);font-weight:700;color:var(--ink);text-align:center}
.sale{left:740px;top:214px;width:76px;height:76px}
.dots{left:576px;top:548px;display:flex;gap:5px}
.dots span{width:10px;height:10px;border-radius:50%;border:2px solid var(--gold);background:transparent}
.dots span.on{background:var(--gold)}

/* product showcase */
.showcase{left:0;top:611px;width:1200px;height:1130px;background:linear-gradient(160deg,#ece4ef 0%,var(--lav-2) 40%,#e3d8e8 70%,#d6c9dd 100%)}
.section-title{left:0;width:1200px;display:flex;justify-content:center;align-items:center;gap:18px}
.section-title .rule{width:90px;height:2px;background:var(--gold)}
.script{font-family:"Satisfy",cursive;font-size:32px;color:var(--gold)}
.script em{font-style:normal;color:var(--blue)}
.photo{background:linear-gradient(135deg,#f4f4f8,#dde2f0)}
.main-photo{left:163px;top:731px;width:265px;height:271px;border:2px solid #555;border-radius:6px;background:#fff}
.thumb{left:443px;width:87px;height:73px;background:#fff;border-radius:3px}
.product-name{left:700px;top:727px;width:320px;text-align:center;font-family:"Lato",sans-serif;font-weight:700;font-size:19px}
.product-name em{font-style:normal;color:var(--blue)}
.old-price{font-size:13px;color:var(--rust);text-decoration:line-through}
.new-price{font-size:19px;font-weight:700;color:var(--blue)}
.cart-btn{left:824px;top:811px;width:165px;height:37px;background:var(--blue);color:#fff;font-size:10px;font-weight:700;text-align:center;line-height:37px;border-radius:2px}
.product-desc{left:690px;top:898px;width:345px;text-align:center;font-family:"Montserrat",sans-serif;font-size:11px;line-height:23px;color:var(--ink)}
.tab{top:1072px;height:39px;font-size:10px;font-weight:700;text-align:center;line-height:39px}
.tab-active{left:241px;width:142px;background:#fff;color:var(--ink)}
.tab-alt{left:398px;width:145px;background:var(--gold);color:#fff}
.tab-panel{left:241px;top:1111px;width:718px;height:213px;background:#fff;padding:30px 0 0 109px;font-family:"Montserrat",sans-serif;font-size:11px;line-height:21.5px}
.tab-panel p{width:520px}
.testi-title{left:0;top:1352px;width:1200px;text-align:center;font-family:"Playfair Display",serif;font-size:26px;color:var(--blue)}
.testi-title em{font-style:normal;color:var(--gold)}
.quote{font-family:"Playfair Display",serif;font-size:190px;color:var(--gold);line-height:1}
.testi-text{left:380px;top:1424px;width:530px;text-align:center;font-family:"Montserrat",sans-serif;font-size:16px;line-height:30px;color:var(--ink)}
.client{display:flex;align-items:center;gap:16px;top:1625px;font-family:"Playfair Display",serif;font-size:14px;color:#8a8a8a}
.avatar{width:59px;height:59px;border-radius:50%;background:linear-gradient(135deg,#b9a6b8,#7d6a78)}
.divider{left:0;top:1738px;width:1200px;height:10px}

/* product rows */
.card{width:169px;height:141px;border:2px solid #8a8a8a;border-radius:3px;background:#fff;box-shadow:0 2px 4px rgba(0,0,0,.15)}
.card .photo{position:absolute;left:20px;top:16px;width:125px;height:105px;border-radius:4px}
.item-name{width:200px;text-align:center;font-family:"Lato",sans-serif;font-weight:700;font-size:12px;line-height:28px}
.item-name em{font-style:normal;color:var(--blue)}
.price-old{font-size:12px;color:var(--rust);text-decoration:line-through}
.price{font-size:16px;font-weight:700;color:var(--blue)}
.buy{width:93px;height:28px;background:var(--blue);color:#fff;font-size:10px;font-weight:700;text-align:center;line-height:28px;border-radius:2px}
.arrow{width:12px;height:22px}

/* footer */
.site-footer{left:0;top:2518px;width:1200px;height:260px;background:var(--footer)}
.foot-links{left:0;top:2580px;width:1200px;display:flex;justify-content:center;gap:16px;font-family:"Playfair Display",serif;font-size:11px;color:#fff}
.foot-links .active{color:var(--gold-soft)}
.foot-social{left:552px;top:2624px}
.foot-social span{background:#fff}
.foot-mail{left:0;top:2683px;width:1200px;display:flex;justify-content:center;gap:90px;font-family:"Montserrat",sans-serif;font-size:12px;color:#fff}
</style>
</head>
<body>

<header class="abs site-header">
  <div class="abs brand"><span class="brand-dot"></span><span class="brand-name">Velvet Ondra</span></div>
  <div class="abs search">search</div>
  <div class="abs search-btn"><svg width="26" height="26" viewBox="0 0 26 26"><circle cx="12" cy="12" r="5" fill="none" stroke="#fff" stroke-width="2"/><line x1="16" y1="16" x2="20" y2="20" stroke="#fff" stroke-width="2"/></svg></div>
  <nav class="abs top-links"><a>HOME</a><a>STORE</a><a>NEED HELP?</a><a class="active">BLOG</a><a>CONTACT</a><a>LOG IN</a></nav>
  <div class="abs social header-social" aria-label="Social media links"><span></span><span></span><span></span></div>
  <svg class="abs cart" viewBox="0 0 30 26"><path d="M2 8h26l-3 16H5z" fill="#0d4d8c"/><path d="M10 8a5 5 0 0 1 10 0" fill="none" stroke="#0d4d8c" stroke-width="2"/></svg>
  <div class="abs cart-info">200$<b>3</b></div>
</header>

<nav class="abs main-nav">
  <a class="current" style="left:224px">MUSICAL INSTRUMENTS ⌄</a>
  <a style="left:419px">CRYSTALS ⌄</a>
  <a style="left:524px">NUMISMATIC COLLECTIBLES</a>
  <a style="left:737px">CULTURAL ARTIFACTS</a>
  <a style="left:915px">ABOUT US</a>
</nav>

<section class="abs hero">
  <svg class="abs hero-bg" viewBox="0 0 1200 460" preserveAspectRatio="none" role="img" aria-label="Collage of antique coins, compass and maps in teal tones">
    <defs><linearGradient id="heroG" x1="0" y1="0" x2="1" y2="1"><stop offset="0" stop-color="#3d9a82"/><stop offset=".5" stop-color="#68b7a1"/><stop offset="1" stop-color="#2f8470"/></linearGradient></defs>
    <path d="M0 0H1200V435Q900 400 600 420T0 440Z" fill="url(#heroG)"/>
  </svg>
  <div class="abs dropdown" style="top:4px">GUITAR<br>VIOLIN<br>PIANO</div>

  <div class="abs promo" style="left:165px;top:142px;width:211px;height:156px">
    <div class="promo-img photo" style="left:10px;top:50px;width:70px;height:56px;background:linear-gradient(135deg,#8a7a66,#4d4238)" role="img" aria-label="Carved wooden artefact"></div>
    <div class="promo-title" style="left:110px;top:46px;font-size:11px">Wood <em>Artefact</em></div>
    <div class="promo-sub" style="left:98px;top:62px;font-size:11px">50% off Only <em>This Week</em></div>
    <div class="shop-btn" style="left:100px;top:88px;width:96px;height:24px;line-height:20px;font-size:8px">SHOP NOW</div>
  </div>

  <div class="abs promo" style="left:404px;top:52px;width:394px;height:294px">
    <div class="promo-img" style="left:34px;top:56px;width:150px;height:150px;border-radius:50%;background:radial-gradient(circle,#7a6f5f,#3f3a32)" role="img" aria-label="Old square-holed coin"></div>
    <div class="promo-title" style="left:244px;top:96px;font-size:19px">Old <em>Coin</em></div>
    <div class="promo-sub" style="left:236px;top:122px;font-size:24px;font-family:'Lato',sans-serif;font-weight:700">20% <em style="font-family:'Satisfy',cursive">Off</em></div>
    <div class="shop-btn" style="left:190px;top:160px;width:178px;height:38px;line-height:34px;font-size:11px">SHOP NOW</div>
  </div>
  <svg class="abs sale" viewBox="0 0 76 76" style="top:38px"><polygon points="38,2 46,18 64,12 58,30 74,38 58,46 64,64 46,58 38,74 30,58 12,64 18,46 2,38 18,30 12,12 30,18" fill="#f2c83a"/><text x="38" y="42" text-anchor="middle" font-family="Lato,sans-serif" font-size="13" font-weight="700" fill="#5a4a10">Sale</text></svg>

  <div class="abs promo" style="left:828px;top:142px;width:211px;height:156px">
    <div class="promo-img" style="left:20px;top:30px;width:56px;height:98px;background:linear-gradient(160deg,#444,#111)" role="img" aria-label="Black electric guitar"></div>
    <div class="promo-title" style="left:112px;top:46px;font-size:11px">Magic <em>Guitar</em></div>
    <div class="promo-sub" style="left:98px;top:62px;font-size:11px">50% off Only <em>This Week</em></div>
    <div class="shop-btn" style="left:100px;top:88px;width:96px;height:24px;line-height:20px;font-size:8px">SHOP NOW</div>
  </div>
  <div class="abs dots" style="top:372px"><span class="on"></span><span></span><span></span></div>
</section>

<section class="abs showcase" role="img" aria-label="Soft background of lavender amethyst crystals" style="z-index:-1"></section>

<h2 class="abs section-title" style="top:630px"><span class="rule"></span><span class="script">Musical <em>Instruments</em></span><span class="rule"></span></h2>

<div class="abs main-photo"><div class="abs photo" style="left:20px;top:30px;width:221px;height:207px" role="img" aria-label="Blue electric guitar"></div></div>
<div class="abs thumb photo" style="top:733px" role="img" aria-label="Blue guitar, front view"></div>
<div class="abs thumb photo" style="top:830px" role="img" aria-label="Blue guitar, angled view"></div>
<div class="abs thumb photo" style="top:928px;height:74px" role="img" aria-label="Blue guitar, close view"></div>

<div class="abs product-name">Mystic <em>Blue Guitar</em></div>
<div class="abs" style="left:724px;top:808px;text-align:center;line-height:20px"><div class="old-price">300$</div><div class="new-price">200$</div></div>
<div class="abs cart-btn">ADD TO CART</div>
<p class="abs product-desc">Lorem ipsum dolor sit amet, consectetur adipiscing elit. Phasellus finibus dolor sed hendrerit vulputate. Etiam consectetur eu leo ac placerat. Curabitur tempus, est id luctus euismod, augue lacus vestibulum ligula, et auctor magna justo eu leo.</p>

<div class="abs tab tab-active">Full Description</div>
<div class="abs tab tab-alt">Characteristics</div>
<div class="abs tab-panel"><p>Lorem ipsum dolor sit amet, consectetur adipiscing elit. Phasellus finibus dolor sed hendrerit vulputate. Etiam consectetur eu leo ac placerat. Curabitur tempus, est id luctus euismod, augue lacus vestibulum ligula, et auctor magna justo eu leo. Aenean scelerisque malesuada erat, sed ultricies urna pretium at.<br>Donec sit amet est et nisi placerat placerat. Vestibulum eu est at ex placerat gravida vel viverra libero. In nec augue nisi. Vivamus aliquam tortor in nisl efficitur, vitae ullamcorper ipsum luctus.</p></div>

<h2 class="abs testi-title">Clients <em>Testimonials</em></h2>
<div class="abs quote" style="left:256px;top:1402px">“</div>
<div class="abs quote" style="left:884px;top:1460px">”</div>
<p class="abs testi-text">Lorem ipsum dolor sit amet, consectetur adipiscing elit. Phasellus vitae mattis nibh, ac interdum ligula. Orci varius natoque penatibus et magnis dis parturient montes, nascetur ridiculus mus. ullamcorper arcu mattis.</p>

<div class="abs client" style="left:272px"><span class="avatar" role="img" aria-label="Client portrait"></span>Marla Venn</div>
<div class="abs client" style="left:531px"><span class="avatar" role="img" aria-label="Client portrait"></span>Oren Talbrook</div>
<div class="abs client" style="left:787px"><span class="avatar" role="img" aria-label="Client portrait"></span>Lisette Corvane</div>

<svg class="abs divider" viewBox="0 0 1200 10"><line x1="0" y1="2" x2="1200" y2="2" stroke="#0d4d8c" stroke-width="1.5"/><line x1="0" y1="7" x2="1200" y2="7" stroke="#0d4d8c" stroke-width="1"/></svg>
<div class="abs" style="left:582px;top:1727px;width:36px;height:36px;border-radius:50%;background:#fff;border:1px solid var(--blue)"></div>

<!-- New -->
<h2 class="abs section-title" style="top:1776px"><span class="rule" style="width:170px;height:1.5px"></span><span class="script" style="font-size:30px">New</span><span class="rule" style="width:170px;height:1.5px"></span></h2>
<svg class="abs arrow" style="left:166px;top:1914px" viewBox="0 0 12 22"><path d="M10 2L2 11l8 9" fill="none" stroke="#b0502d" stroke-width="2"/></svg>
<svg class="abs arrow" style="left:1022px;top:1914px" viewBox="0 0 12 22"><path d="M2 2l8 9-8 9" fill="none" stroke="#b0502d" stroke-width="2"/></svg>

<div class="abs card" style="left:194px;top:1854px"><div class="photo" style="background:linear-gradient(135deg,#f6d27a,#d99a2e)" role="img" aria-label="Yellow crystal cluster"></div></div>
<div class="abs item-name" style="left:178px;top:2003px">Yellow <em>Crystal</em></div>
<div class="abs" style="left:196px;top:2050px;text-align:center;line-height:20px"><div class="price-old">300</div><div class="price">200$</div></div>
<div class="abs buy" style="left:270px;top:2059px">BUY</div>

<div class="abs card" style="left:407px;top:1854px"><div class="photo" style="background:radial-gradient(circle,#7a7468,#3d3a34)" role="img" aria-label="Ancient grey coin"></div></div>
<div class="abs item-name" style="left:391px;top:2003px">Very Old Ancient Gray<br><em>Coin</em></div>
<div class="abs" style="left:409px;top:2050px;text-align:center;line-height:20px"><div class="price-old">200$</div><div class="price">100$</div></div>
<div class="abs buy" style="left:483px;top:2059px">BUY</div>

<div class="abs card" style="left:620px;top:1854px"><div class="photo" style="background:linear-gradient(135deg,#f3eee8,#9a3b1c)" role="img" aria-label="Brown violin"></div></div>
<div class="abs item-name" style="left:604px;top:2003px">Luxurious Brown <em>Violin</em></div>
<div class="abs" style="left:626px;top:2050px;text-align:center;line-height:20px"><div class="price-old">150$</div><div class="price">50$</div></div>
<div class="abs buy" style="left:696px;top:2059px">BUY</div>

<div class="abs card" style="left:833px;top:1854px"><div class="photo" style="background:linear-gradient(135deg,#a49c8e,#4e4a42)" role="img" aria-label="Ancient artefact"></div></div>
<div class="abs item-name" style="left:817px;top:2003px">Ancient <em>Artefact</em></div>
<div class="abs price" style="left:834px;top:2064px">300$</div>
<div class="abs buy" style="left:909px;top:2059px">BUY</div>

<!-- Popular -->
<h2 class="abs section-title" style="top:2124px"><span class="rule" style="width:170px;height:1.5px"></span><span class="script" style="font-size:30px">Popular</span><span class="rule" style="width:170px;height:1.5px"></span></h2>
<svg class="abs arrow" style="left:166px;top:2262px" viewBox="0 0 12 22"><path d="M10 2L2 11l8 9" fill="none" stroke="#b0502d" stroke-width="2"/></svg>
<svg class="abs arrow" style="left:1022px;top:2262px" viewBox="0 0 12 22"><path d="M2 2l8 9-8 9" fill="none" stroke="#b0502d" stroke-width="2"/></svg>

<div class="abs card" style="left:194px;top:2200px"><div class="photo" style="background:linear-gradient(135deg,#b9b3a4,#6e6a5e)" role="img" aria-label="Pile of old coins"></div></div>
<div class="abs item-name" style="left:178px;top:2350px">Set Of Old <em>Coins</em></div>
<div class="abs" style="left:196px;top:2398px;text-align:center;line-height:20px"><div class="price-old">300</div><div class="price">200$</div></div>
<div class="abs buy" style="left:270px;top:2406px">BUY</div>

<div class="abs card" style="left:407px;top:2230px"><div class="photo" style="background:linear-gradient(135deg,#e8d8c4,#8a5a34)" role="img" aria-label="Brown bead necklace"></div></div>
<div class="abs item-name" style="left:391px;top:2379px">Lady's Luxurious Brown<br><em>Beads</em></div>
<div class="abs" style="left:409px;top:2426px;text-align:center;line-height:20px"><div class="price-old">150$</div><div class="price">50$</div></div>
<div class="abs buy" style="left:483px;top:2436px">BUY</div>

<div class="abs card" style="left:620px;top:2200px"><div class="photo" style="background:linear-gradient(135deg,#f2eac8,#2f7a4e)" role="img" aria-label="Ancient ring with green stone"></div></div>
<div class="abs item-name" style="left:604px;top:2350px">Ancient <em>Jewelry</em></div>
<div class="abs price" style="left:621px;top:2411px">300$</div>
<div class="abs buy" style="left:696px;top:2406px">BUY</div>

<div class="abs card" style="left:833px;top:2230px"><div class="photo" style="background:linear-gradient(135deg,#f3e2a0,#a88a2a)" role="img" aria-label="Yellow cut crystal"></div></div>
<div class="abs item-name" style="left:817px;top:2379px">Magic Yellow <em>Crystal</em></div>
<div class="abs price" style="left:834px;top:2440px">300$</div>
<div class="abs buy" style="left:909px;top:2436px">BUY</div>

<footer class="abs site-footer" role="img" aria-label="Dark background with faint gemstones"></footer>
<nav class="abs foot-links"><a>HOME</a><a>STORE</a><a>NEED HELP?</a><a class="active">BLOG</a><a>CONTACT</a><a>LOG IN</a></nav>
<div class="abs social foot-social" aria-label="Social media links"><span></span><span></span><span></span></div>
<div class="abs foot-mail"><span>sales@velvetondra.com</span><span>info@velvetondra.com</span></div>

</body>
</html>
```